Ferris Contracting LLC Business Card Design

I am looking for a creative and unique business card design. We are a commercial construction general contractor. With the name "FERRIS" Contracting, I am hoping to see some neat designs that correlate with the name.

```html
<!DOCTYPE html>
<html lang="en">
<head>
<meta charset="utf-8">
<title>Ferris Contracting LLC – Business Card</title>
<link href="https://fonts.googleapis.com/css2?family=Michroma&family=Oswald:wght@300;400&display=swap" rel="stylesheet">
<style>
  :root {
    --page: #ffffff;
    --card-dark: #1a1a1b;
    --card-mid: #2b2b2c;
    --band: #101011;
    --steel-light: #8e8e8e;
    --steel-dark: #3a3a3b;
    --brand-blue: #1f86d1;
    --text-light: #f4f4f4;
  }
  * { margin: 0; padding: 0; box-sizing: border-box; }
  html, body {
    width: 1200px; height: 1200px; overflow: hidden;
    background: var(--page);
  }
  .canvas { position: relative; width: 1200px; height: 1200px; }

  .card {
    position: absolute; left: 253px; width: 651px; height: 372px;
    overflow: hidden;
    background: radial-gradient(ellipse at 60% 35%, var(--card-mid), var(--card-dark) 75%);
  }
  .card--front { top: 218px; }
  .card--back { top: 641px; }

  .card__art { position: absolute; inset: 0; width: 651px; height: 372px; }

  /* Front */
  .person { position: absolute; left: 31px; top: 29px; }
  .person__name {
    font-family: "Michroma", sans-serif; color: var(--text-light);
    font-size: 25px; font-weight: 400; letter-spacing: 0.5px; line-height: 1;
  }
  .person__role {
    font-family: "Michroma", sans-serif; color: var(--brand-blue);
    font-size: 13.5px; letter-spacing: 1.6px; margin-top: 8px; line-height: 1;
  }
  .contact { position: absolute; left: 22px; top: 95px; list-style: none; }
  .contact__item {
    display: flex; align-items: flex-start; gap: 8px;
    font-family: "Oswald", sans-serif; font-weight: 300;
    color: var(--text-light); font-size: 21px; line-height: 1.1;
    margin-bottom: 6px;
  }
  .contact__item span { padding-top: 2px; }
  .contact__icon { width: 29px; height: 29px; flex: none; }

  .brand {
    position: absolute; display: flex; align-items: center; gap: 12px;
    font-family: "Michroma", sans-serif; color: var(--brand-blue);
  }
  .brand__mark {
    width: 22px; height: 22px; border-radius: 50%;
    background: var(--brand-blue); flex: none;
  }
  .brand__name { line-height: 1.1; }
  .brand__word { display: block; }
  .brand--front { left: 318px; top: 118px; font-size: 54px; }
  .brand--front .brand__sub { font-size: 16px; letter-spacing: 7.2px; margin-top: 2px; }
  .brand--back { left: 372px; top: 48px; font-size: 38px; }
  .brand--back .brand__sub { font-size: 12px; letter-spacing: 4.6px; }

  /* Back */
  .tagline {
    position: absolute; left: 67px; top: 150px;
    font-family: "Michroma", sans-serif; color: var(--text-light);
    font-size: 19.5px; font-weight: 400; letter-spacing: 0.6px; white-space: nowrap;
  }
  .services { position: absolute; left: 58px; top: 195px; list-style: none; }
  .services__item {
    display: flex; align-items: center; gap: 12px;
    font-family: "Michroma", sans-serif; color: var(--text-light);
    font-size: 17.5px; letter-spacing: 0.5px; height: 31px;
  }
  .services__item::before {
    content: ""; width: 14px; height: 14px; border-radius: 50%;
    background: var(--brand-blue); flex: none;
  }
</style>
</head>
<body>
<main class="canvas">

  <!-- Front of card -->
  <section class="card card--front">
    <svg class="card__art" viewBox="0 0 651 372">
      <defs>
        <linearGradient id="frontStripTone" x1="0" y1="0" x2="0" y2="1">
          <stop offset="0" stop-color="var(--steel-dark)" stop-opacity="0"/>
          <stop offset="0.45" stop-color="var(--steel-dark)" stop-opacity="0.7"/>
          <stop offset="1" stop-color="var(--steel-light)" stop-opacity="0.45"/>
        </linearGradient>
      </defs>
      <rect x="0" y="212" width="651" height="160" fill="url(#frontStripTone)"
            role="img" aria-label="Illustration area: jagged steel strip with welding sparks across the lower card"/>
    </svg>

    <div class="person">
      <h1 class="person__name">DANIEL MERCER</h1>
      <p class="person__role">PROJECT MANAGER</p>
    </div>

    <ul class="contact">
      <li class="contact__item">
        <svg class="contact__icon" viewBox="0 0 30 30"><circle cx="15" cy="15" r="13.5" fill="none" stroke="var(--brand-blue)" stroke-width="1.5"/><path d="M10 8.5l3 0 1.2 3.5-1.8 1.3a8 8 0 0 0 4.3 4.3l1.3-1.8 3.5 1.2v3a1.5 1.5 0 0 1-1.6 1.5A12 12 0 0 1 8.5 10.1 1.5 1.5 0 0 1 10 8.5z" fill="var(--brand-blue)"/></svg>
        <span>(555) 014-2276</span>
      </li>
      <li class="contact__item">
        <svg class="contact__icon" viewBox="0 0 30 30"><circle cx="15" cy="15" r="13.5" fill="none" stroke="var(--brand-blue)" stroke-width="1.5"/><rect x="11" y="7.5" width="8" height="15" rx="1.5" fill="none" stroke="var(--brand-blue)" stroke-width="1.5"/></svg>
        <span>daniel@ferriscontracting.com</span>
      </li>
      <li class="contact__item">
        <svg class="contact__icon" viewBox="0 0 30 30"><circle cx="15" cy="15" r="13.5" fill="none" stroke="var(--brand-blue)" stroke-width="1.5"/><rect x="8.5" y="10.5" width="13" height="9" fill="var(--brand-blue)"/><path d="M8.5 10.5l6.5 5 6.5-5" fill="none" stroke="var(--card-dark)" stroke-width="1.2"/></svg>
        <span>4410 Foundry Rd, Millbrook,<br>USA 40217</span>
      </li>
    </ul>

    <div class="brand brand--front">
      <span class="brand__mark"></span>
      <span class="brand__name">
        <span class="brand__word">FERRIS</span>
        <span class="brand__word brand__sub">CONTRACTING</span>
      </span>
    </div>
  </section>

  <!-- Back of card -->
  <section class="card card--back">
    <svg class="card__art" viewBox="0 0 651 372">
      <defs>
        <linearGradient id="backTopTone" x1="0" y1="0" x2="1" y2="1">
          <stop offset="0" stop-color="var(--steel-light)" stop-opacity="0.55"/>
          <stop offset="1" stop-color="var(--steel-dark)" stop-opacity="0"/>
        </linearGradient>
        <radialGradient id="backBottomTone" cx="1" cy="1" r="1">
          <stop offset="0" stop-color="var(--steel-light)" stop-opacity="0.6"/>
          <stop offset="1" stop-color="var(--steel-dark)" stop-opacity="0"/>
        </radialGradient>
      </defs>
      <rect x="0" y="0" width="300" height="118" fill="url(#backTopTone)"
            role="img" aria-label="Illustration area: torn steel plate with welding sparks, top left"/>
      <rect x="0" y="114" width="651" height="217" fill="var(--band)" opacity="0.7"/>
      <rect x="280" y="140" width="371" height="232" fill="url(#backBottomTone)"
            role="img" aria-label="Illustration area: torn steel plate with welding sparks, bottom right"/>
    </svg>

    <div class="brand brand--back">
      <span class="brand__mark"></span>
      <span class="brand__name">
        <span class="brand__word">FERRIS</span>
        <span class="brand__word brand__sub">CONTRACTING</span>
      </span>
    </div>

    <h2 class="tagline">COMMERICAL GENERAL CONTRACTOR</h2>
    <ul class="services">
      <li class="services__item">GENERAL CONTRACTING</li>
      <li class="services__item">DESIGN-BUILD</li>
      <li class="services__item">CONSTRUCTION MANAGEMENT</li>
    </ul>
  </section>

</main>
</body>
</html>
```